BUSINESS book cover

Publishing a book for a specific industry and hope to customize it for different industries in the future. So, design needs to be flexible. I want BRIGHT (possibly orange) cover with large words for title...really do not need illustration. Just the subtitle will change for future editions. Book is going to be 5.25" x 8"

Sorry for any confusion. The title of the book is: "Once You Reach a Yes..." The subtitle is: A Comprehensive Member Expderience Guide for Today's Club Management Professional

```html
<!DOCTYPE html>
<html lang="en">
<head>
<meta charset="utf-8">
<title>Once You Reach a Yes... — Book Cover</title>
<link href="https://fonts.googleapis.com/css2?family=Lexend:wght@500&family=Open+Sans:wght@400;700&family=Source+Sans+3:wght@300;400;700&display=swap" rel="stylesheet">
<style>
  :root {
    --backdrop: #666666;
    --orange: #f7a128;
    --white: #ffffff;
    --ink: #222222;
    --grey-text: #555555;
    --spine-grey: #6a6a6a;
    --gold-light: #e6c36e;
    --gold-dark: #b68a34;
  }
  * { margin: 0; padding: 0; box-sizing: border-box; }
  html, body { width: 1200px; height: 1000px; overflow: hidden; background: var(--backdrop); }
  .spread { position: absolute; left: 50px; top: 80px; width: 1100px; height: 838px; background: var(--white); overflow: hidden; }
  .bands { position: absolute; inset: 0; }

  /* back cover */
  .back { position: absolute; left: 0; top: 0; width: 525px; height: 838px; }
  .back-heading { position: absolute; left: 95px; top: 89px; width: 390px; text-align: center;
    font-family: "Source Sans 3", sans-serif; font-size: 20px; line-height: 22px; color: var(--grey-text); font-weight: 400; letter-spacing: .3px; }
  .back-copy { position: absolute; left: 100px; top: 170px; width: 378px;
    font-family: "Open Sans", sans-serif; font-size: 10.4px; line-height: 16px; color: var(--ink); text-align: justify; }
  .back-copy p { margin-bottom: 6px; }
  .back-copy p.gap { margin-top: 18px; }
  .back-copy .lead { font-weight: 700; margin-top: 10px; margin-bottom: 0; }
  .back-copy ul { list-style: none; text-align: left; }
  .back-copy li::before { content: "• "; }
  .back-copy .more { margin-top: 8px; }
  .author-photo { position: absolute; left: 0; top: 612px; width: 196px; height: 126px;
    background: linear-gradient(135deg, #c4c4c4, #7a7a7a 60%, #3a3a3a); }
  .author-bio { position: absolute; left: 210px; top: 609px; width: 268px;
    font-family: "Open Sans", sans-serif; font-size: 8.6px; line-height: 14.3px; color: var(--ink); }
  .author-bio b { font-weight: 700; }
  .author-bio .booking { margin-top: 12px; font-weight: 700; }

  /* spine */
  .spine { position: absolute; left: 525px; top: 0; width: 25px; height: 838px; }
  .spine-label { position: absolute; white-space: nowrap; font-family: "Source Sans 3", sans-serif; transform: rotate(-90deg); transform-origin: left top; }
  .spine-label.audience { left: 3px; top: 510px; font-size: 17.5px; letter-spacing: 1.1px; color: var(--white); font-weight: 400; }
  .spine-label.name { left: 4px; top: 765px; font-size: 15.5px; color: var(--spine-grey); font-weight: 300; }
  .spine-label b { font-weight: 700; }

  /* front cover */
  .front { position: absolute; left: 550px; top: 0; width: 550px; height: 838px; }
  .front-author { position: absolute; right: 45px; top: 62px; font-family: "Source Sans 3", sans-serif;
    font-size: 27px; color: var(--grey-text); font-weight: 300; }
  .front-author b { font-weight: 700; }
  .front-title { position: absolute; right: 38px; top: 168px; text-align: right; font-family: "Lexend", sans-serif;
    font-size: 62px; line-height: 67px; color: var(--white); font-weight: 500; letter-spacing: -.5px; }
  .front-subtitle { position: absolute; right: 42px; top: 414px; width: 500px; text-align: right;
    font-family: "Source Sans 3", sans-serif; font-weight: 300; font-size: 22.5px; line-height: 34px; color: var(--white); }
  .hero-image { position: absolute; left: 230px; top: 535px; width: 200px; height: 250px;
    background: linear-gradient(160deg, var(--gold-light), var(--gold-dark)); }
</style>
</head>
<body>
<main class="spread">
  <svg class="bands" width="1100" height="838" viewBox="0 0 1100 838" aria-hidden="true">
    <defs>
      <linearGradient id="spineShade" x1="0" x2="1">
        <stop offset="0" stop-color="#000" stop-opacity="0"/>
        <stop offset="1" stop-color="#000" stop-opacity=".08"/>
      </linearGradient>
      <linearGradient id="frontShade" x1="0" x2="1">
        <stop offset="0" stop-color="#000" stop-opacity=".08"/>
        <stop offset="1" stop-color="#000" stop-opacity="0"/>
      </linearGradient>
    </defs>
    <polygon points="0,572 525,528 525,838 0,838" fill="var(--orange)"/>
    <rect x="525" y="0" width="25" height="526" fill="var(--orange)"/>
    <polygon points="550,0 1100,0 1100,485 550,525" fill="var(--orange)"/>
    <rect x="440" y="0" width="85" height="838" fill="url(#spineShade)"/>
    <rect x="550" y="0" width="60" height="838" fill="url(#frontShade)"/>
  </svg>

  <section class="back">
    <h2 class="back-heading">THIS BOOK IS FOR<br>CLUB MANAGEMENT PROFESSIONALS<br>ONLY!</h2>
    <div class="back-copy">
      <p>Why is Bellwood Coffee so successful in selling you a $4.00 cup of coffee when QuickBite charges $2.00? Why does a stay at a Grand Aubrey hotel seem much different than at a stay at the Roadway Lodge?</p>
      <p>Most people today would answer that it’s all about ‘customer service’ when, in fact, they would be wrong! Both QuickBite and Roadway Lodge offer incredible customer service. What Bellwood Coffee and Grand Aubrey understand is that it is about the customer EXPERIENCE!</p>
      <p class="gap">Much attention is given to the member experience in this profession, but do we really understand what needs to be done to take our club to the next level? “Once You Reach a Yes…” is a comprehensive book with assessments, surveys and examples personalized to the club management profession.</p>
      <p class="lead">In reading this book, you will be able to:</p>
      <ul>
        <li>Analyze and tweak our member touch points</li>
        <li>Create a “touch point map” specific to your club</li>
        <li>Assess whether or not your strategy will be successful</li>
        <li>Be more innovative in managing your people and your members</li>
        <li>Take an innovation survey</li>
        <li>Establish your club’s “Declaration of Experience”</li>
        <li>Distinguish between employee engagement and employee satisfaction</li>
      </ul>
      <p class="more">And much, much more</p>
    </div>
    <div class="author-photo" role="img" aria-label="Black and white portrait photograph of the author"></div>
    <div class="author-bio">
      <p><b>Dale Mercer</b> M. Ed, CSP has been working with club professionals for 15+ years. His first book, “Thinking Past the Fence” has long been an industry favorite and his sessions at NCPA nationally and for individual clubs have made him a leading expert in creative thinking as it applies to the member experience.</p>
      <p class="booking">For more information on booking Dale,<br>visit www.DaleMercer.com or call him directly at<br>555-014-2870</p>
    </div>
  </section>

  <section class="spine">
    <span class="spine-label audience">FOR CLUB MANAGEMENT PROFESSIONALS</span>
    <span class="spine-label name"><b>Dale Mercer</b> M. Ed, CSP</span>
  </section>

  <section class="front">
    <p class="front-author"><b>Dale Mercer</b> M. Ed, CSP</p>
    <h1 class="front-title">Once You<br>Reach a<br>Yes...</h1>
    <p class="front-subtitle">A Comprehensive Member Expderience Guide for<br>Today’s Club&nbsp; Management Professional</p>
    <div class="hero-image" role="img" aria-label="Cover photograph of a golden object on white"></div>
  </section>
</main>
</body>
</html>
```